Professional DJ Business Card

Business card for giving out to clubs and venues or interested groups that are in need of a professional DJ. I want something artistic and catchy/alluring, with a minimalist approach that gets just the vital amount of info and leaves the rest for inquiry via contacting me. Ideally I would like one side to have an image of something cool like an eye and my name, then the other side be the contact info, I am definitely feeling a black or dark colored card, but I am open to other designs. I am uploading a picture that I made that reflects a little of what I am *kind of* looking for.

Industry/Entity Type

Business

Contact Information for Business Card

Tomas Velander (Kalvo)
Professional DJ (West Coast)
EDM (Deep/House/Techno), Hip Hop, Latin, Trap.
Cell: 555-274-8391
Email: Kalvoofficial@mailbrook.net
www.tunevault.net/oxfernwaits

```html
<!DOCTYPE html>
<html lang="en">
<head>
<meta charset="utf-8">
<title>Kalvo – Professional DJ Business Card</title>
<link rel="stylesheet" href="https://fonts.googleapis.com/css2?family=Fira+Sans+Condensed:wght@400;500;600;800&display=swap">
<style>
  :root {
    --bg: #d9d9d9;
    --card-dark: #231f20;
    --orange: #f07f1f;
    --orange-deep: #d8661a;
    --ink: #1b1b1b;
    --white: #ffffff;
  }
  * { box-sizing: border-box; margin: 0; padding: 0; }
  html, body {
    width: 1200px;
    height: 814px;
    overflow: hidden;
  }
  body {
    background: var(--bg);
    font-family: "Fira Sans Condensed", "Arial Narrow", sans-serif;
    position: relative;
  }
  .card {
    position: absolute;
    width: 560px;
    height: 320px;
    box-shadow: 0 6px 18px rgba(0,0,0,0.25);
  }

  /* Front side */
  .card-front {
    left: 560px;
    top: 90px;
    background: linear-gradient(135deg, var(--orange-deep) 0%, var(--orange) 100%);
    display: flex;
    flex-direction: column;
    align-items: center;
    justify-content: center;
    gap: 18px;
  }
  .brand-mark {
    width: 110px;
    height: 110px;
    border-radius: 50%;
    background: var(--ink);
  }
  .brand-name {
    font-weight: 800;
    font-size: 64px;
    color: var(--ink);
    letter-spacing: 1px;
    line-height: 1;
  }

  /* Back side */
  .card-back {
    left: 100px;
    top: 400px;
    background: var(--card-dark);
    color: var(--white);
    padding: 30px 34px;
  }
  .identity-line {
    display: flex;
    align-items: baseline;
    gap: 12px;
    line-height: 1;
  }
  .dj-name {
    font-weight: 600;
    font-size: 26px;
  }
  .dj-alias {
    font-weight: 600;
    font-size: 26px;
    color: var(--orange);
  }
  .dj-role {
    color: var(--orange);
    font-size: 15px;
    font-weight: 500;
    margin-top: 2px;
  }
  .dj-genres {
    font-size: 13px;
    margin-top: 2px;
    letter-spacing: 0.2px;
  }
  .contact {
    position: absolute;
    right: 40px;
    bottom: 34px;
    font-size: 17px;
    line-height: 1.3;
  }
  .contact-row {
    display: grid;
    grid-template-columns: 62px auto;
  }
  .contact-label { color: var(--orange); }
  .accent { color: var(--orange); }
</style>
</head>
<body>
  <section class="card card-front" aria-label="Business card front">
    <div class="brand-mark"></div>
    <div class="brand-name">Kalvo</div>
  </section>

  <section class="card card-back" aria-label="Business card back">
    <div class="identity">
      <div class="identity-line">
        <span class="dj-name">Tomas Velander</span>
        <span class="dj-alias">Kalvo</span>
      </div>
      <div class="dj-role">Professional DJ</div>
      <div class="dj-genres">EDM Deep House Techno Hip Hop Latin Trap</div>
    </div>

    <div class="contact">
      <div class="contact-row">
        <span class="contact-label">Cell:</span>
        <span>555-274-8391 <span class="accent">,</span> West Coast</span>
      </div>
      <div class="contact-row">
        <span class="contact-label">Email:</span>
        <span>Kalvoofficial<span class="accent">@</span>mailbrook.net</span>
      </div>
      <div class="contact-web">www.tunevault.net<span class="accent">/</span>oxfernwaits</div>
    </div>
  </section>
</body>
</html>
```